Speisekarten-Design für Gastronomiebetrieb
Zielgruppe
Wir sind ein Gastronomiebetrieb in einer Studentenstadt. Unsere Hauptzielgruppe sind junge Menschen und Studenten, aber auch älteres Puplikum. Wir möchten gerne ein neues Speisekartendesign, da unser aktuelles seit über 10 Jahren sich kaum verändert hat.
Aufgabenstellung
Gerne könne Sie sich die aktulle Speisekarte auf der unserer Hompeage anschauen: www.tomello-kassel.de
Auf der Frontseite soll die Farbrichtung Orange und natürlich das Logo beibehalten werden. Für die restlichen Seiten gibt es diese Einschränkung nicht. Uns ist wichtig, dass die Speisekarte modern, bunt und peppig ist. Das heisst möglichst mit kräftigen Farben und Bildern von Speisen und Getränken arbeiten.

```html
<!DOCTYPE html>
<html lang="de">
<head>
<meta charset="utf-8">
<title>Tomello – Speisekarte: Aktionen &amp; Frühstück</title>
<link href="https://fonts.googleapis.com/css2?family=Fjalla+One&family=Fira+Sans:wght@400;500&display=swap" rel="stylesheet">
<style>
  :root {
    --backdrop: #e6e6e6;
    --page-orange: #e9962b;
    --page-orange-dark: #d88420;
    --accent-red: #e53d1f;
    --heading-red: #d9301b;
    --text-white: #fff7ea;
    --rule: rgba(255, 245, 225, 0.75);
    --paper: #f7f7f5;
  }
  * { box-sizing: border-box; margin: 0; padding: 0; }
  html, body { width: 1200px; height: 900px; overflow: hidden; background: var(--backdrop); }
  body { position: relative; font-family: "Fira Sans", sans-serif; color: var(--text-white); }

  .spread { position: absolute; left: 20px; top: 147px; width: 1160px; height: 606px; display: flex; }
  .page { position: relative; height: 606px; overflow: hidden; background: var(--page-orange); }
  .page--left { width: 567px; background: linear-gradient(to right, var(--page-orange) 92%, var(--page-orange-dark)); }
  .page--right { width: 593px; background: linear-gradient(to left, var(--page-orange) 93%, var(--page-orange-dark)); }

  .banner { position: absolute; left: 0; top: 0; }
  .banner-title {
    position: absolute; font-family: "Fjalla One", sans-serif; color: #fff;
    text-transform: uppercase; line-height: 1; letter-spacing: 0.5px;
  }
  .page--left .banner-title { left: 35px; top: 33px; font-size: 23px; line-height: 24px; }
  .page--right .banner-title { left: 35px; top: 33px; font-size: 23px; }

  /* Offers column */
  .offers { position: absolute; left: 263px; top: 46px; width: 198px; }
  .offer { border-bottom: 1px solid var(--rule); padding-bottom: 14px; margin-bottom: 16px; font-family: "Fjalla One", sans-serif; text-transform: uppercase; }
  .offer-title { color: var(--heading-red); font-size: 22px; line-height: 24px; letter-spacing: 0.3px; }
  .offer-main { color: var(--text-white); font-size: 13px; line-height: 18px; }
  .offer-note { color: var(--text-white); font-size: 9px; line-height: 15px; letter-spacing: 0.2px; }
  .footnote { position: absolute; left: 263px; top: 574px; font-size: 8px; color: var(--text-white); }

  /* Photo frames */
  .photo { position: absolute; background: var(--paper); box-shadow: 2px 3px 8px rgba(0,0,0,0.25); padding: 11px 11px 30px; }
  .photo-fill { width: 100%; height: 100%; }
  .photo--pizza { left: 6px; top: 150px; width: 215px; height: 270px; transform: rotate(5deg); }
  .photo--pizza .photo-fill { background: radial-gradient(circle at 60% 45%, #e5a84c, #b8562a 55%, #8a6a48); }
  .photo--casserole { left: 20px; top: 394px; width: 165px; height: 198px; transform: rotate(-4deg); }
  .photo--casserole .photo-fill { background: radial-gradient(circle at 50% 50%, #e6d8b4, #c4452a 60%, #6e3820); }
  .photo--waffles { left: 190px; top: 520px; width: 152px; height: 110px; transform: rotate(2deg); }
  .photo--waffles .photo-fill { background: linear-gradient(135deg, #c98b4a, #d23a3a 60%, #8a2a25); }
  .photo--bread { left: 362px; top: 492px; width: 208px; height: 140px; transform: rotate(-3deg); }
  .photo--bread .photo-fill { background: linear-gradient(120deg, #4a3424, #e9b06a 50%, #f3ede2); }

  /* Opening hours note */
  .hours-note { position: absolute; left: 0; top: 0; }
  .hours-text { position: absolute; left: 358px; top: 22px; transform: rotate(-5deg); transform-origin: left top; color: var(--heading-red); }
  .hours-line { font-family: "Fjalla One", sans-serif; font-size: 14px; line-height: 15px; }
  .hours-sub { font-size: 9px; line-height: 13px; margin-top: 4px; font-style: italic; }

  /* Breakfast menu */
  .menu-col { position: absolute; top: 130px; }
  .menu-col--a { left: 35px; width: 242px; }
  .menu-col--b { left: 312px; width: 245px; }
  .col-divider { position: absolute; left: 296px; top: 127px; width: 1px; height: 394px; background: var(--accent-red); }
  .dish { border-bottom: 1px solid var(--rule); padding-bottom: 12px; margin-bottom: 12px; }
  .dish:last-child { border-bottom: none; }
  .dish-head { display: flex; justify-content: space-between; font-family: "Fjalla One", sans-serif; text-transform: uppercase; color: var(--heading-red); font-size: 14px; line-height: 17px; }
  .dish-desc { font-size: 10px; line-height: 15px; font-weight: 500; color: var(--text-white); }
  .dish-desc sup { font-size: 5px; vertical-align: 4px; }
</style>
</head>
<body>
<main class="spread">
  <section class="page page--left">
    <svg class="banner" width="230" height="125" viewBox="0 0 230 125" aria-hidden="true">
      <polygon points="0,0 220,0 229,93 0,123" fill="var(--accent-red)"/>
    </svg>
    <h1 class="banner-title">Aktionen<br>und Angebote</h1>

    <figure class="photo photo--pizza"><div class="photo-fill" role="img" aria-label="Foto einer Pizza mit Tomaten und Kräutern"></div></figure>
    <figure class="photo photo--casserole"><div class="photo-fill" role="img" aria-label="Foto eines überbackenen Auflaufs mit Tomaten und Oliven"></div></figure>

    <div class="offers">
      <article class="offer">
        <h2 class="offer-title">Montag Auflauftag</h2>
        <p class="offer-main">Alle Aufläufe 5,90€</p>
        <p class="offer-note">Garnelen- und Lachs-Auflauf 6,50€</p>
      </article>
      <article class="offer">
        <h2 class="offer-title">Sonntagsbrunch</h2>
        <p class="offer-main">10.00 Uhr – 15.00 Uhr, 13,90€</p>
        <p class="offer-note">Warmes und kaltes Buffet inkl. Kaffee, Tee,<br>Orangen- und Multivitaminsaft</p>
      </article>
      <article class="offer">
        <h2 class="offer-title">Sonntag Pizzatag</h2>
        <p class="offer-main">Alle Pizzen 5,90€*</p>
        <p class="offer-note">Pizza New York und Pizza Texas 6,90€</p>
      </article>
      <article class="offer">
        <h2 class="offer-title">Tägliche Happy Hour</h2>
        <p class="offer-main">18.00 – 20.00 und<br>23.00 – 24.00 Uhr</p>
        <p class="offer-note">Alle Cocktails für 5,50€</p>
      </article>
      <article class="offer">
        <h2 class="offer-title">Abholer-Rabatt</h2>
        <p class="offer-main">10 % bei Selbstabholung*</p>
        <p class="offer-note">Auf alle Pizzen, Aufläufe und Salate</p>
      </article>
    </div>
    <p class="footnote">*nicht mit anderen Angeboten kombinierbar</p>
  </section>

  <section class="page page--right">
    <svg class="banner" width="240" height="125" viewBox="0 0 240 125" aria-hidden="true">
      <polygon points="0,0 212,0 222,93 0,123" fill="var(--accent-red)"/>
    </svg>
    <h1 class="banner-title">Frühstück</h1>

    <svg class="hours-note" width="593" height="110" viewBox="0 0 593 110" aria-hidden="true">
      <polygon points="343,0 593,0 593,77 352,103" fill="var(--paper)"/>
    </svg>
    <div class="hours-text">
      <p class="hours-line">Mo–Do: 10–13 Uhr</p>
      <p class="hours-line">Fr–Sa: 10–15 Uhr</p>
      <p class="hours-sub">Zu jedem Frühstück gibt es Kaffee<br>und Tee, so viel Sie möchten</p>
    </div>

    <div class="col-divider"></div>

    <div class="menu-col menu-col--a">
      <article class="dish">
        <h3 class="dish-head"><span>Kleines Frühstück</span><span>4,50 €</span></h3>
        <p class="dish-desc">1 Vollkornbrötchen, Butter, Marmelade</p>
      </article>
      <article class="dish">
        <h3 class="dish-head"><span>Großes Frühstück</span><span>6,90 €</span></h3>
        <p class="dish-desc">2 Brötchen mit Butter, Marmelade,<br>Schinken<sup>2,3,7,hs</sup>, Käse<sup>1,2,16</sup>, Salami<sup>2,3</sup>,<br>1 Ei und 1 Milchkaffee</p>
      </article>
      <article class="dish">
        <h3 class="dish-head"><span>Französisches Frühstück</span><span>7,10 €</span></h3>
        <p class="dish-desc">2 Brötchen, 1 Croissant, Butter, Marmela-<br>de, Honig, Nussola, Käse<sup>1,2,16</sup>, Salami<sup>2,3</sup> und<br>1 Glas Orangensaft</p>
      </article>
      <article class="dish">
        <h3 class="dish-head"><span>Frühstück Tomello</span><span>7,50 €</span></h3>
        <p class="dish-desc">1 Vollkornbrötchen, 1 Croissant, Butter,<br>Marmelade, 1 Spiegelei, Schinken<sup>2,3,7,hs</sup>,<br>Käse<sup>1,2,16</sup>, Salami<sup>2,3</sup> und 1 Glas Orangensaft</p>
      </article>
      <article class="dish">
        <h3 class="dish-head"><span>Frühstück Kassel</span><span>7,50 €</span></h3>
        <p class="dish-desc">2 Brötchen, Butter, Marmelade,<br>3 Rühreier, Schinken<sup>2,3,7,hs</sup>,<br>Tomaten und 1 Milchkaffee</p>
      </article>
    </div>

    <div class="menu-col menu-col--b">
      <article class="dish">
        <h3 class="dish-head"><span>Fitness Frühstück</span><span>7,90 €</span></h3>
        <p class="dish-desc">2 Vollkornbrötchen, Butter, geräucherte<br>Putenbrust, frisches Obst und Frisch-<br>käse<sup>16</sup>, dazu 1 Glas Orangensaft</p>
      </article>
      <article class="dish">
        <h3 class="dish-head"><span>Meerrettich Frühstück</span><span>8,50 €</span></h3>
        <p class="dish-desc">2 Brötchen, Schinken<sup>2,3,7,hs</sup>, Meerrettich,<br>1 Ei, frisches Obst, Kräuterquark, und<br>1 Cappuccino</p>
      </article>
      <article class="dish">
        <h3 class="dish-head"><span>Sekt-Frühstück</span><span>8,50 €</span></h3>
        <p class="dish-desc">1 Vollkornbrötchen, 1 Croissant, Räucher-<br>lachs mit Sahne-Meerrettich-Sauce,<br>Butter, Kräuterquark, Tomaten, Mozza-<br>rella und 1 Glas Sekt</p>
      </article>
      <article class="dish">
        <h3 class="dish-head"><span>Frühstück „Lola Sommer“</span><span>7,90 €</span></h3>
        <p class="dish-desc">Frische Waffeln mit Honig, Marmelade,<br>Nussola, Fruchtjoghurt, Butter, Toastbrot<br>und frischem Obst</p>
      </article>
    </div>

    <figure class="photo photo--waffles"><div class="photo-fill" role="img" aria-label="Foto von Waffeln mit Kirschen"></div></figure>
    <figure class="photo photo--bread"><div class="photo-fill" role="img" aria-label="Foto von belegten Vollkornbroten mit Frischkäse und Gemüse"></div></figure>
  </section>
</main>
</body>
</html>
```